Create a banner for me that embodies my health and well being package.

I am an intuitive counselor with a busy practice helping clients to shift their blocks and move forward in their lives.
I have created a package called '9 paths home again'
I am wanting a banner to put on my website page, facebook page and to use as a letter head in mailouts.
My ideal clients are those who want to create change in their lives and who invest money in themselves and their personal and spiritual growth.
I am different to regular life coaches as my sessions have a spiritual twist to them creating much deeper change in my clients.
I would like the banner to be mainly font with the title of the progam: 9 Paths Home Again (no other wording) (something along the lines of the Blackjack font) and that ties in with the theme of my website. I'm not sure what else I want with it and am looking for ideas.
Website:
www.brightwillowhealing.com.au
I also have a current facebook page for the business:
https://www.facebook.com/Brightwillow-Healing-Studio-502718364091547/
(Note: I am about to drop my logo and business name and move to using my own name - the rest of the website will remain the same).
I have attached a doc with the draft of what wording will be on the website page any advertising will link to, to give you an idea of what the program is about.

Target Market(s)

People who invest money on themselves who are looking to improve their emotional well being and creating change in their life. Majority are middle aged women (also younger females and some men)

Industry/Entity Type

Health And Wellness

Font styles to use
Other font styles liked:
• I like Blackjack and Amienne. Along those lines.

Requirements
Must have
• Attractive, modern and GREAT font.
Nice to have
• Surprise me with something amazing!
• I love the colours in the 2 images I have up loaded as they represent the heart chakra colours. They could be a feature on the banner or blurred into the background.
Should not have
• Even though my work is quite spiritual I don't want it to look woo woo (meaning airy fairy spiritual stuff!)

```html
<!DOCTYPE html>
<html lang="en">
<head>
<meta charset="UTF-8">
<title>9 Paths Home Again – Banner</title>
<link rel="stylesheet" href="https://fonts.googleapis.com/css2?family=Dancing+Script:wght@500&family=Arimo:wght@400&display=swap">
<style>
  :root {
    --leaf-deep: #3f5a22;
    --leaf-mid: #6f8f3a;
    --leaf-light: #a7bf6a;
    --petal-pink: #e8559a;
    --petal-soft: #f39ac4;
    --petal-deep: #c2306f;
    --text-white: #ffffff;
  }
  html, body {
    margin: 0;
    padding: 0;
    width: 1200px;
    height: 444px;
    overflow: hidden;
    background: #ffffff;
  }
  .banner {
    position: relative;
    width: 1200px;
    height: 444px;
    overflow: hidden;
  }
  .banner__backdrop {
    position: absolute;
    inset: 0;
    background:
      radial-gradient(ellipse 330px 230px at 470px 210px, var(--petal-soft) 0%, var(--petal-pink) 40%, rgba(232,85,154,0) 100%),
      radial-gradient(ellipse 260px 160px at 520px 400px, rgba(60,70,110,0.55) 0%, rgba(60,70,110,0) 100%),
      radial-gradient(ellipse 420px 300px at 1050px 120px, var(--leaf-light) 0%, rgba(167,191,106,0) 100%),
      linear-gradient(100deg, var(--leaf-deep) 0%, var(--leaf-mid) 45%, var(--leaf-mid) 70%, var(--leaf-deep) 100%);
  }
  .banner__content {
    position: absolute;
    inset: 0;
    text-align: center;
    color: var(--text-white);
    text-shadow: 0 1px 6px rgba(80, 20, 50, 0.35);
  }
  .banner__title {
    position: absolute;
    left: 0;
    right: 0;
    top: 176px;
    margin: 0;
    font-family: "Dancing Script", cursive;
    font-weight: 500;
    font-size: 86px;
    line-height: 1;
  }
  .banner__tagline {
    position: absolute;
    left: 0;
    right: 0;
    top: 291px;
    margin: 0;
    font-family: "Arimo", sans-serif;
    font-size: 19px;
  }
  .banner__website {
    position: absolute;
    left: 0;
    right: 0;
    top: 366px;
    margin: 0;
    font-family: "Arimo", sans-serif;
    font-size: 18px;
  }
</style>
</head>
<body>
  <div class="banner">
    <div class="banner__backdrop" role="img" aria-label="Soft-focus photograph of a pink lotus flower against blurred green leaves"></div>
    <div class="banner__content">
      <h1 class="banner__title">9 paths home again</h1>
      <p class="banner__tagline">Seeing the world from the eyes of your heart.</p>
      <p class="banner__website">www.clarawrenfield.com.au</p>
    </div>
  </div>
</body>
</html>
```